Picture Ads

We need some banner ads for our home business opportunity, we are evolving from text to picture ads. I have added some examples of what other distributors are using. We are looking for something really eye catching with some good key words and nice bright colours and to include our photo (attached)
Key words to include:
Booming online business
Personal Development and Leadership Industry
Earn an executive income from home
Simple 3 step system
Make up to $5,000 per sale
Not MLM
The size needs to be: 1000 x 35 pixels
13.9 x 4.75 Inches
35.3 x 11.1 cm
I think different platforms accept different sizes, not too familiar with it yet, any guidance welcome. I've clicked project for 2 days if that is to prioritise the order?
Many thanks,
Maren

Industry/Entity Type

Business

```html
<!DOCTYPE html>
<html lang="en">
<head>
<meta charset="utf-8">
<title>Home Business Banner</title>
<link rel="stylesheet" href="https://fonts.googleapis.com/css2?family=Cabin+Condensed:wght@700&display=swap">
<style>
  :root {
    --haze: #e4e8df;
    --grass-light: #b9d98a;
    --grass-mid: #86c04a;
    --grass-deep: #4f8f25;
    --bullet: #4a4f4a;
    --pill-edge: #5a5f5a;
    --ink: #0d0d0d;
    --halo: #ffffff;
    --sky-a: #4fa3a0;
    --sky-b: #cfe3c0;
    --sky-c: #e8efc4;
    --sun-a: #f3d75a;
    --sun-b: #fff4b8;
    --sun-c: #e9b53a;
    --stone-a: #c9b48a;
    --stone-b: #f0d99a;
    --stone-c: #a89868;
    --garden-a: #9bb26a;
    --garden-b: #e6d7a2;
    --garden-c: #c8b57e;
  }
  html, body {
    margin: 0;
    padding: 0;
    overflow: hidden;
    background: #ffffff;
  }
  .banner {
    position: relative;
    width: 1200px;
    height: 420px;
    overflow: hidden;
    font-family: "Cabin Condensed", "Arial Narrow", sans-serif;
  }
  .banner__scene {
    position: absolute;
    inset: 0;
    background:
      radial-gradient(ellipse 520px 300px at 180px 80px, rgba(240,242,236,0.95), rgba(240,242,236,0) 75%),
      radial-gradient(ellipse 600px 260px at 900px 120px, rgba(210,225,190,0.7), rgba(210,225,190,0) 80%),
      linear-gradient(180deg, var(--haze) 0%, var(--grass-light) 40%, var(--grass-mid) 70%, var(--grass-deep) 100%);
  }
  .features {
    position: absolute;
    left: 0;
    top: 0;
    margin: 0;
    padding: 0;
    list-style: none;
  }
  .feature {
    position: absolute;
    left: 0;
    width: 660px;
    height: 66px;
  }
  .feature:nth-child(1) { top: 48px; }
  .feature:nth-child(2) { top: 134px; }
  .feature:nth-child(3) { top: 220px; }
  .feature:nth-child(4) { top: 304px; }
  .feature__bullet {
    position: absolute;
    left: 14px;
    top: 24px;
    width: 22px;
    height: 22px;
    background: var(--bullet);
  }
  .feature__pill {
    position: absolute;
    left: 50px;
    top: 0;
    width: 598px;
    height: 66px;
    box-sizing: border-box;
    border: 3px solid var(--pill-edge);
    border-radius: 33px;
    overflow: hidden;
    box-shadow: inset 0 0 0 2px rgba(255,255,255,0.55), 0 1px 3px rgba(0,0,0,0.35);
  }
  .feature__photo {
    position: absolute;
    inset: 0;
  }
  .feature__photo--sky {
    background: linear-gradient(90deg, var(--sky-a) 0%, var(--sky-b) 45%, var(--sky-c) 100%);
  }
  .feature__photo--sunset {
    background: linear-gradient(90deg, var(--sun-c) 0%, var(--sun-a) 35%, var(--sun-b) 70%, var(--sun-a) 100%);
  }
  .feature__photo--castle {
    background: linear-gradient(90deg, var(--stone-c) 0%, var(--stone-a) 35%, var(--stone-b) 70%, var(--sun-a) 100%);
  }
  .feature__photo--garden {
    background: linear-gradient(180deg, var(--garden-b) 0%, var(--garden-c) 45%, var(--garden-a) 100%);
  }
  .feature__text {
    position: absolute;
    left: 0;
    right: 0;
    top: 0;
    height: 60px;
    margin: 0;
    line-height: 60px;
    text-align: center;
    font-size: 44px;
    font-weight: 700;
    color: var(--ink);
    letter-spacing: -0.5px;
    white-space: nowrap;
    text-shadow:
      2px 0 0 var(--halo), -2px 0 0 var(--halo), 0 2px 0 var(--halo), 0 -2px 0 var(--halo),
      2px 2px 0 var(--halo), -2px -2px 0 var(--halo), 2px -2px 0 var(--halo), -2px 2px 0 var(--halo),
      0 0 6px rgba(255,255,255,0.9);
  }
</style>
</head>
<body>
  <div class="banner">
    <div class="banner__scene" role="img" aria-label="Close-up photo of bright green grass blades in soft morning light"></div>
    <ul class="features">
      <li class="feature">
        <span class="feature__bullet"></span>
        <div class="feature__pill">
          <div class="feature__photo feature__photo--sky" role="img" aria-label="Photo of a teal sky over green fields"></div>
          <p class="feature__text">Make up to $5,000 per sale!</p>
        </div>
      </li>
      <li class="feature">
        <span class="feature__bullet"></span>
        <div class="feature__pill">
          <div class="feature__photo feature__photo--sunset" role="img" aria-label="Photo of a golden sunset sky"></div>
          <p class="feature__text">Booming online business!</p>
        </div>
      </li>
      <li class="feature">
        <span class="feature__bullet"></span>
        <div class="feature__pill">
          <div class="feature__photo feature__photo--castle" role="img" aria-label="Photo of a stone castle in warm evening light"></div>
          <p class="feature__text">Not MLM!</p>
        </div>
      </li>
      <li class="feature">
        <span class="feature__bullet"></span>
        <div class="feature__pill">
          <div class="feature__photo feature__photo--garden" role="img" aria-label="Photo of castle grounds with green trees and lawn"></div>
          <p class="feature__text">Simple 3 step system!</p>
        </div>
      </li>
    </ul>
  </div>
</body>
</html>
```